Business card like design

Hello we need a business card like design, not with personal info. But with info from our shop, like address, phone, street, email, facebook .....
This cards we put in the box when we send out the orders......
Target Market(s)
We sell cheap sunglasses, our customers are mainly young adults, that like going to parties
Industry/Entity Type
Business

```html
<!DOCTYPE html>
<html lang="nl">
<head>
<meta charset="utf-8">
<title>brightshades.nl – shop card</title>
<link rel="stylesheet" href="https://fonts.googleapis.com/css2?family=Exo+2:wght@500;600&family=Open+Sans:wght@400&display=swap">
<style>
  :root {
    --backdrop: #d9d9d7;
    --card-dark: #231f20;
    --card-dark-soft: #383435;
    --card-white: #ffffff;
    --accent-orange: #f7963a;
    --icon-fill: #f8cf9f;
    --text-light: #ffffff;
  }
  * { margin: 0; padding: 0; box-sizing: border-box; }
  html, body { width: 1200px; height: 793px; overflow: hidden; background: var(--backdrop); }
  .canvas { position: relative; width: 1200px; height: 793px; }

  .card {
    position: absolute;
    top: 248px;
    width: 520px;
    height: 297px;
    overflow: hidden;
    box-shadow: 0 6px 18px rgba(0,0,0,.18);
  }

  /* Front side */
  .card-front { left: 50px; background: var(--card-dark); }
  .front-wordmark {
    position: absolute;
    left: 0; right: 0; top: 50%;
    transform: translateY(-50%);
    text-align: center;
    font-family: "Exo 2", sans-serif;
    font-weight: 600;
    font-size: 44px;
    letter-spacing: 1px;
    color: var(--text-light);
  }

  /* Back side */
  .card-back { left: 630px; background: var(--card-white); }
  .info-panel {
    position: absolute;
    right: 0; top: 0;
    width: 200px; height: 100%;
    background: var(--card-dark);
  }
  .accent-corner { position: absolute; left: 268px; top: 0; }

  .back-logo {
    position: absolute;
    left: 0; width: 320px; top: 50%;
    transform: translateY(-50%);
    display: flex; align-items: center; justify-content: center; gap: 10px;
  }
  .back-logo .logo-dot {
    width: 22px; height: 22px; border-radius: 50%;
    background: var(--accent-orange);
  }
  .back-logo .logo-name {
    font-family: "Exo 2", sans-serif;
    font-weight: 600;
    font-size: 30px;
    color: var(--card-dark);
  }

  .vertical-name {
    position: absolute;
    right: -2px; top: 0;
    width: 297px;
    transform-origin: top left;
    transform: translateX(297px) rotate(90deg) translateY(-28px);
    font-family: "Exo 2", sans-serif;
    font-weight: 500;
    font-size: 24px;
    letter-spacing: 1px;
    color: var(--card-dark-soft);
    padding-left: 4px;
    line-height: 28px;
  }

  .contact-list {
    position: absolute;
    right: 34px; top: 104px;
    list-style: none;
    font-family: "Open Sans", sans-serif;
    font-size: 10.5px;
    line-height: 1.45;
    color: var(--accent-orange);
    text-align: right;
  }
  .contact-item { display: flex; align-items: center; justify-content: flex-end; gap: 8px; margin-bottom: 14px; }
  .contact-item .icon {
    flex: none;
    width: 20px; height: 20px; border-radius: 50%;
    background: var(--icon-fill);
    display: flex; align-items: center; justify-content: center;
  }
</style>
</head>
<body>
<main class="canvas">

  <section class="card card-front" aria-label="Card front">
    <p class="front-wordmark">brightshades.nl</p>
  </section>

  <section class="card card-back" aria-label="Card back">
    <svg class="accent-corner" width="52" height="56" viewBox="0 0 52 56" aria-hidden="true">
      <polygon points="0,0 52,0 52,56" fill="var(--accent-orange)"/>
    </svg>

    <div class="back-logo">
      <span class="logo-dot"></span>
      <span class="logo-name">brightshades.nl</span>
    </div>

    <div class="info-panel">
      <div class="vertical-name">brightshades.nl</div>
      <ul class="contact-list">
        <li class="contact-item">
          <span>Parkweg 12 4811 AB<br>Breda Nederland</span>
          <span class="icon">
            <svg width="10" height="12" viewBox="0 0 10 12" aria-hidden="true"><path d="M5 0C2.2 0 0 2.1 0 4.7 0 8 5 12 5 12s5-4 5-7.3C10 2.1 7.8 0 5 0zm0 6.6A1.9 1.9 0 1 1 5 2.8a1.9 1.9 0 0 1 0 3.8z" fill="var(--card-dark)"/></svg>
          </span>
        </li>
        <li class="contact-item">
          <span>003176 512 34 80</span>
          <span class="icon">
            <svg width="12" height="10" viewBox="0 0 12 10" aria-hidden="true"><path d="M1 3c0-1.5 2.5-2.5 5-2.5S11 1.5 11 3v1H8.5V2.8h-5V4H1zM2.5 5h7l1 4.5h-9z" fill="var(--card-dark)"/></svg>
          </span>
        </li>
        <li class="contact-item">
          <span>info@BrightShades.nl</span>
          <span class="icon">
            <svg width="12" height="9" viewBox="0 0 12 9" aria-hidden="true"><rect x="0.5" y="0.5" width="11" height="8" fill="none" stroke="var(--card-dark)"/><path d="M0.5 0.5 6 5l5.5-4.5" fill="none" stroke="var(--card-dark)"/></svg>
          </span>
        </li>
        <li class="contact-item">
          <span>social: @brightshades</span>
          <span class="icon"></span>
        </li>
      </ul>
    </div>
  </section>

</main>
</body>
</html>
```